Real Estate Office Front Facade Redesign - ideas needed

Kindly read this brief thoroughly as there are 2 deliverables:
1. Office building façade redesign (see attached logo and also photo of our office building façade)
2. I also require a design for a freestanding signboard that will be coordinated with the design of the office front please see the images attached labelled signboard.

Deliverable number 1:
I am looking for a minimalist contemporary design with strong colours to draw the attention of the passing Traffic.

The office facade is to be repainted so you may choose to recolour the office in any way to coordinate with logo however the attached logo must remain as is. I prefer the colours red black and white or shades of these colours.

Vireo property managers is a new company looking to target property investors in the local area. Most of our clients are from a middle to upper income demographic. We help these investors to rent out their properties and ensure they are maintained in good condition and provide a regular income.

The area we operate in is centrally located and close to the central business district of Perth.

Our office is situated in a residential area on a busy road facing diagonally at 45° down the road. People see our office from their cars whilst driving to work, there is no pedestrian traffic in the area. Therefore the office façade needs to stand out and any signage must be read by quickly passing traffic or convey our brand in seconds. Whilst the view of the office from the road is obscured somewhat by trees from a distance, once within 50 to 100 m of the office the full face of the office front is visible facing directly at the driver.

No measurements are provided for the façade of the office (please see the photo provided), this is a blank canvas as the whole building will be repainted to fit in with YOUR design. A logo is also attached. The colours red black and white are preferred.

Please provide an image of the office with signage/colours superimposed.

Deliverable number 2:
Also attached is an image of a freestanding sign for which I require a design. This sign is used for advertising properties for lease or sale which will be erected outside the front of residential houses. Again this sign needs to be bold and bright with a contemporary design. It needs to stand out from the crowd of many other signs in the area, whilst the sign advertises the property it must also promote our company brand by having a prominent logo. The size of these signboards will either be 1250 mm x 900 mm or 1800 mm x 625 mm. Please note that this sign must be rectangular in shape and cannot have any text or logo protruding outside of the lines of the rectangular sign due to cost restrictions.

Target Market(s)

Industry/Entity Type

Real Estate

Font styles to use
Sans Serif

Colors
ec1f27
ffffff
000000

Requirements
Must have
• Contemporary uncluttered design using the colours red black and white of shades of.
Nice to have
• A prominent logo with the words "Property Managers" easily read by passing traffic.
• Files provided with editable text and the name of the font used.
Should not have
• designs protruding outside of the overall building facia or sign rectangle.

```html
<!DOCTYPE html>
<html lang="en">
<head>
<meta charset="utf-8">
<title>Vireo Property Managers – For Lease or Sale Signboard</title>
<link rel="stylesheet" href="https://fonts.googleapis.com/css2?family=Crimson+Text:wght@700&family=Cabin:wght@400&display=swap">
<style>
  :root {
    --brand-red: #ec1f27;
    --shadow-red: #8a0f14;
    --panel-white: #eef4f4;
    --ink: #2a2a2a;
    --page: #e9ebee;
    --white: #ffffff;
  }
  * { margin: 0; padding: 0; box-sizing: border-box; }
  html, body {
    width: 1200px;
    height: 799px;
    overflow: hidden;
    background: var(--page);
  }
  .signboard {
    position: absolute;
    left: 90px;
    top: 18px;
    width: 1020px;
    height: 763px;
    display: flex;
    flex-direction: column;
    box-shadow: 0 6px 24px rgba(0,0,0,0.18);
  }
  .signboard__headline {
    height: 493px;
    background: var(--brand-red);
    display: flex;
    flex-direction: column;
    align-items: center;
    justify-content: center;
    padding-bottom: 8px;
  }
  .headline__line {
    font-family: "Crimson Text", Georgia, serif;
    font-weight: 700;
    font-size: 168px;
    line-height: 210px;
    color: var(--white);
    text-shadow: 5px 5px 0 var(--shadow-red);
    letter-spacing: 1px;
  }
  .signboard__details {
    height: 231px;
    background: var(--panel-white);
    position: relative;
  }
  .brand {
    position: absolute;
    left: 36px;
    top: 36px;
    width: 220px;
    display: flex;
    flex-direction: column;
    align-items: center;
  }
  .brand__square {
    width: 62px;
    height: 62px;
    background: var(--brand-red);
    margin-bottom: 14px;
  }
  .brand__name,
  .brand__descriptor {
    font-family: "Cabin", Arial, sans-serif;
    font-weight: 400;
    color: var(--ink);
    text-transform: uppercase;
  }
  .brand__name {
    font-size: 46px;
    line-height: 44px;
    letter-spacing: 6px;
  }
  .brand__descriptor {
    font-size: 12px;
    letter-spacing: 1.5px;
    margin-top: 4px;
  }
  .contact {
    position: absolute;
    left: 390px;
    right: 30px;
    top: 26px;
    text-align: center;
    font-family: "Cabin", Arial, sans-serif;
    font-weight: 400;
    font-size: 42px;
    line-height: 59px;
    color: var(--ink);
    list-style: none;
  }
  .signboard__strip {
    height: 39px;
    background: var(--brand-red);
  }
</style>
</head>
<body>
  <section class="signboard" aria-label="Property signboard">
    <header class="signboard__headline">
      <h1 class="headline__line">For Lease</h1>
      <p class="headline__line">or Sale</p>
    </header>
    <div class="signboard__details">
      <div class="brand">
        <span class="brand__square" aria-hidden="true"></span>
        <span class="brand__name">Vireo</span>
        <span class="brand__descriptor">Property managers</span>
      </div>
      <ul class="contact">
        <li>Mobile 0400 1234 5678</li>
        <li>Office 9300 1234</li>
        <li>www.vireoproperty.com.au</li>
      </ul>
    </div>
    <div class="signboard__strip"></div>
  </section>
</body>
</html>
```